Mobil Battery Sales and Instalation

We are a automotive roadside svc company. I am looking to focus on battery sales and instalation We offer tire changes, lockuot, jump starts fuel delivry and battery sales This design should be battery sales and instalation focused My company name is. Ridgeway Roadside Svcs. 707-216-3847 call or text Hours 7am to 9pm. Free service call and instalation with purchase of new battery. Free testing Free battery disposal Colors we like are black and orange or red and black

Target Market(s)

Automotive, RV, Comerical truck, motorcycle and boat

Industry/Entity Type

Automotive

Requirements
Must have
• Pic of battery
• Mobil battery service.
Nice to have
• I want people to see this card and know its a mobil service for battery sales and installation. But can see we offer other services.
• Use my company name but i dont want that to be the standout. (Tuck it in somewhere).
Should not have
• No pictures of any trucks cars etc.
• we do not tow!

```html
<!DOCTYPE html>
<html lang="en">
<head>
<meta charset="utf-8">
<title>Ridgeway Roadside Svcs – Battery Service Offer</title>
<link rel="stylesheet" href="https://fonts.googleapis.com/css2?family=Arimo:wght@400;700&display=swap">
<style>
  :root {
    --panel-black: #231f20;
    --offer-orange: #f7941d;
    --icon-red: #e31e24;
    --paper-white: #ffffff;
  }
  html, body {
    margin: 0;
    padding: 0;
    overflow: hidden;
    background: var(--paper-white);
  }
  .card {
    position: relative;
    width: 1200px;
    height: 814px;
    background: var(--paper-white);
    font-family: "Arimo", Arial, sans-serif;
    overflow: hidden;
  }
  .offer-panel {
    position: absolute;
    left: 0;
    top: 0;
    width: 1200px;
    height: 556px;
    background: var(--panel-black);
    color: var(--offer-orange);
    text-align: center;
  }
  .offer-headline {
    position: absolute;
    left: 0;
    width: 100%;
    margin: 0;
    font-weight: 700;
    font-size: 45px;
    line-height: 1;
    letter-spacing: 0.5px;
  }
  .offer-headline--service { top: 184px; }
  .offer-headline--testing { top: 361px; }
  .offer-headline--disposal { top: 447px; }
  .offer-detail {
    position: absolute;
    left: 0;
    top: 272px;
    width: 100%;
    margin: 0;
    font-weight: 400;
    font-size: 32px;
    line-height: 1;
  }
  .service-icons {
    position: absolute;
    left: 0;
    top: 593px;
    width: 1200px;
    height: 144px;
    margin: 0;
    padding: 0;
    list-style: none;
  }
  .service-icon {
    position: absolute;
    top: 0;
    width: 144px;
    height: 144px;
  }
  .service-icon svg { display: block; width: 144px; height: 144px; }
  .service-icon--roadside { left: 174px; }
  .service-icon--testing  { left: 342px; }
  .service-icon--tires    { left: 522px; }
  .service-icon--lockout  { left: 698px; }
  .service-icon--jump     { left: 866px; }
</style>
</head>
<body>
<main class="card">
  <section class="offer-panel">
    <h1 class="offer-headline offer-headline--service">FREE SERVICE</h1>
    <p class="offer-detail">call and instillation with purchase of new battery.</p>
    <p class="offer-headline offer-headline--testing">FREE TESTING</p>
    <p class="offer-headline offer-headline--disposal">FREE BATTERY DISPOSAL.</p>
  </section>

  <ul class="service-icons">
    <li class="service-icon service-icon--roadside">
      <svg viewBox="0 0 144 144" role="img" aria-label="Roadside assistance pictogram">
        <circle cx="72" cy="72" r="66" fill="none" stroke="var(--icon-red)" stroke-width="10"/>
        <circle cx="72" cy="72" r="50" fill="var(--icon-red)" opacity="0.85"/>
      </svg>
    </li>
    <li class="service-icon service-icon--testing">
      <svg viewBox="0 0 144 144" role="img" aria-label="Battery testing gauge">
        <circle cx="72" cy="72" r="66" fill="none" stroke="var(--icon-red)" stroke-width="10"/>
        <path d="M30 84 A42 42 0 0 1 114 84" fill="none" stroke="var(--icon-red)" stroke-width="9"/>
        <g stroke="var(--icon-red)" stroke-width="5" stroke-linecap="round">
          <line x1="42" y1="66" x2="48" y2="70"/>
          <line x1="55" y1="50" x2="59" y2="57"/>
          <line x1="72" y1="44" x2="72" y2="52"/>
          <line x1="89" y1="50" x2="85" y2="57"/>
          <line x1="102" y1="66" x2="96" y2="70"/>
          <line x1="72" y1="82" x2="88" y2="58" stroke-width="6"/>
        </g>
        <circle cx="72" cy="82" r="6" fill="var(--icon-red)"/>
        <rect x="46" y="96" width="52" height="12" fill="var(--icon-red)"/>
      </svg>
    </li>
    <li class="service-icon service-icon--tires">
      <svg viewBox="0 0 144 144" role="img" aria-label="Tire change wheel">
        <circle cx="72" cy="72" r="70" fill="var(--icon-red)"/>
        <circle cx="72" cy="72" r="46" fill="none" stroke="var(--paper-white)" stroke-width="8"/>
        <g stroke="var(--paper-white)" stroke-width="8" stroke-linecap="round">
          <line x1="72" y1="72" x2="72" y2="30"/>
          <line x1="72" y1="72" x2="112" y2="59"/>
          <line x1="72" y1="72" x2="97" y2="106"/>
          <line x1="72" y1="72" x2="47" y2="106"/>
          <line x1="72" y1="72" x2="32" y2="59"/>
        </g>
        <circle cx="72" cy="72" r="12" fill="var(--paper-white)"/>
        <circle cx="72" cy="72" r="5" fill="var(--icon-red)"/>
      </svg>
    </li>
    <li class="service-icon service-icon--lockout">
      <svg viewBox="0 0 144 144" role="img" aria-label="Lockout service key">
        <circle cx="72" cy="72" r="66" fill="none" stroke="var(--icon-red)" stroke-width="10"/>
        <circle cx="58" cy="88" r="16" fill="none" stroke="var(--icon-red)" stroke-width="9"/>
        <g stroke="var(--icon-red)" stroke-width="9" stroke-linecap="round">
          <line x1="70" y1="76" x2="102" y2="44"/>
          <line x1="94" y1="52" x2="102" y2="60"/>
          <line x1="86" y1="60" x2="92" y2="66"/>
        </g>
      </svg>
    </li>
    <li class="service-icon service-icon--jump">
      <svg viewBox="0 0 144 144" role="img" aria-label="Jump start cables">
        <circle cx="72" cy="72" r="66" fill="none" stroke="var(--icon-red)" stroke-width="10"/>
        <path d="M40 104 C50 70 84 90 92 58" fill="none" stroke="var(--icon-red)" stroke-width="6"/>
        <g transform="rotate(-45 98 48)">
          <rect x="88" y="30" width="20" height="34" rx="4" fill="var(--icon-red)"/>
          <rect x="92" y="20" width="4" height="12" fill="var(--icon-red)"/>
          <rect x="100" y="20" width="4" height="12" fill="var(--icon-red)"/>
        </g>
        <circle cx="40" cy="104" r="6" fill="var(--icon-red)"/>
      </svg>
    </li>
  </ul>
</main>
</body>
</html>
```